Bref créative
Quorel Stationary
Stationary and Business Cards
I need double sided standard sized Business Card [3.5" x 2"]
show me your ideas
Corporate
Marcus Toddin
Chief Executive Officer
Halvenor Business Tower
18th Floor
PO Box 58217
Dubai
United Arab Emirates
mt@quorel.co
www.quorel.co
Show me your ideas

```html
<!DOCTYPE html>
<html lang="en">
<head>
<meta charset="utf-8">
<title>Quorel Stationary</title>
<link href="https://fonts.googleapis.com/css2?family=Open+Sans:wght@400;600&display=swap" rel="stylesheet">
<style>
:root{
  --board:#3a3b3d;
  --paper:#ffffff;
  --blue:#1e9fdc;
  --blue-deep:#0d7fc0;
  --blue-soft:#bfe4f6;
  --grey-line:#b9bcc0;
  --ink:#5a5f66;
}
*{margin:0;padding:0;box-sizing:border-box}
html,body{width:1200px;height:310px;overflow:hidden;background:var(--board);font-family:"Open Sans",Arial,sans-serif}
.board{position:relative;width:1200px;height:310px}
.piece{position:absolute;background:var(--paper);overflow:hidden;box-shadow:0 2px 6px rgba(0,0,0,.45)}
.swoosh{position:absolute;left:0;bottom:0;width:100%;display:block}
.brand{position:absolute;display:flex;align-items:center;gap:4px;color:var(--blue-deep);font-weight:600}
.brand-dot{border-radius:50%;background:var(--blue)}
.details{position:absolute;color:var(--ink);line-height:1.35}

.sticker{position:absolute;left:24px;top:20px;width:84px;height:84px;border-radius:50%;
  background:radial-gradient(circle at 40% 35%,#6cc6ef,var(--blue-deep));box-shadow:0 2px 6px rgba(0,0,0,.5);
  display:flex;align-items:center;justify-content:center;color:#fff;font-weight:600;font-size:15px}

.card-small{left:12px;top:120px;width:96px;height:54px}
.card-front{left:19px;top:211px;width:120px;height:54px}
.card-back{left:144px;top:211px;width:120px;height:54px;
  background:linear-gradient(135deg,#5fc2ee,var(--blue-deep));display:flex;align-items:center;justify-content:center}
.card-back .brand-name{color:#fff;font-weight:600;font-size:13px}

.letterhead-a{left:283px;top:19px;width:178px;height:269px}
.letterhead-b{left:480px;top:19px;width:180px;height:269px}
.env-front-a{left:696px;top:43px;width:216px;height:111px}
.env-front-b{left:696px;top:180px;width:216px;height:108px}
.env-open{left:936px;top:24px;width:240px;height:120px;background:#f2f3f4}
.env-closed{left:936px;top:180px;width:240px;height:108px;background:#f7f8f9}
.flap{position:absolute;left:0;top:0;width:100%;height:100%}
</style>
</head>
<body>
<main class="board">

  <div class="sticker">Quorel</div>

  <section class="piece card-small">
    <div class="brand" style="left:6px;top:6px;font-size:7px"><span class="brand-dot" style="width:7px;height:7px"></span>Quorel</div>
    <div class="details" style="left:6px;top:18px;font-size:4px">Marcus Toddin<br>mt@quorel.co</div>
    <svg class="swoosh" viewBox="0 0 100 20" preserveAspectRatio="none" height="14"><path d="M0 9 Q50 22 100 4 L100 20 L0 20Z" fill="var(--blue)"/><path d="M0 6 Q50 19 100 1" fill="none" stroke="var(--grey-line)" stroke-width="1"/></svg>
  </section>

  <section class="piece card-front">
    <div class="brand" style="left:7px;top:7px;font-size:8px"><span class="brand-dot" style="width:8px;height:8px"></span>Quorel</div>
    <div class="details" style="left:64px;top:7px;font-size:4px">Marcus Toddin<br>Chief Executive Officer<br>mt@quorel.co<br>www.quorel.co</div>
    <svg class="swoosh" viewBox="0 0 100 20" preserveAspectRatio="none" height="14"><path d="M0 9 Q50 22 100 4 L100 20 L0 20Z" fill="var(--blue)"/><path d="M0 6 Q50 19 100 1" fill="none" stroke="var(--grey-line)" stroke-width="1"/></svg>
  </section>

  <section class="piece card-back"><span class="brand-name">Quorel</span></section>

  <section class="piece letterhead-a">
    <div class="brand" style="left:12px;top:10px;font-size:9px"><span class="brand-dot" style="width:12px;height:12px"></span>Quorel</div>
    <div class="details" style="right:12px;top:10px;font-size:4px;text-align:left">Halvenor Business Tower, 18th Floor<br>PO Box 58217, Dubai<br>United Arab Emirates<br>mt@quorel.co · www.quorel.co</div>
    <svg class="swoosh" viewBox="0 0 100 20" preserveAspectRatio="none" height="38"><path d="M0 8 Q50 22 100 2 L100 20 L0 20Z" fill="var(--blue)"/><path d="M0 11 Q50 24 100 6 L100 20 L0 20Z" fill="var(--blue-soft)" opacity=".5"/><path d="M0 5 Q50 19 100 0" fill="none" stroke="var(--grey-line)" stroke-width=".8"/></svg>
  </section>

  <section class="piece letterhead-b">
    <div class="brand" style="left:12px;top:10px;font-size:9px"><span class="brand-dot" style="width:12px;height:12px"></span>Quorel</div>
    <svg class="swoosh" viewBox="0 0 100 20" preserveAspectRatio="none" height="38"><path d="M0 8 Q50 22 100 2 L100 20 L0 20Z" fill="var(--blue)"/><path d="M0 11 Q50 24 100 6 L100 20 L0 20Z" fill="var(--blue-soft)" opacity=".5"/><path d="M0 5 Q50 19 100 0" fill="none" stroke="var(--grey-line)" stroke-width=".8"/></svg>
  </section>

  <section class="piece env-front-a">
    <div class="brand" style="left:8px;top:8px;font-size:8px"><span class="brand-dot" style="width:10px;height:10px"></span>Quorel</div>
    <div class="details" style="left:46px;top:10px;font-size:4px">Halvenor Business Tower<br>PO Box 58217, Dubai<br>www.quorel.co</div>
    <svg class="swoosh" viewBox="0 0 100 20" preserveAspectRatio="none" height="26"><path d="M0 9 Q50 22 100 3 L100 20 L0 20Z" fill="var(--blue)"/><path d="M0 6 Q50 19 100 0" fill="none" stroke="var(--grey-line)" stroke-width=".8"/></svg>
  </section>

  <section class="piece env-front-b">
    <div class="brand" style="left:8px;top:8px;font-size:8px"><span class="brand-dot" style="width:10px;height:10px"></span>Quorel</div>
    <svg class="swoosh" viewBox="0 0 100 20" preserveAspectRatio="none" height="28"><path d="M0 9 Q50 22 100 3 L100 20 L0 20Z" fill="var(--blue)"/><path d="M0 6 Q50 19 100 0" fill="none" stroke="var(--grey-line)" stroke-width=".8"/></svg>
  </section>

  <section class="piece env-open">
    <svg class="flap" viewBox="0 0 240 120" preserveAspectRatio="none"><path d="M0 0 L120 46 L240 0Z" fill="#d9dcdf"/><path d="M0 120 L120 58 L240 120Z" fill="#ffffff"/><path d="M0 0 L120 58 L0 120Z" fill="#eceef0"/><path d="M240 0 L120 58 L240 120Z" fill="#e6e8ea"/><circle cx="120" cy="70" r="9" fill="var(--blue)"/></svg>
  </section>

  <section class="piece env-closed">
    <svg class="flap" viewBox="0 0 240 108" preserveAspectRatio="none"><path d="M0 0 L120 60 L240 0Z" fill="#ffffff" stroke="#d5d8db"/><path d="M0 108 L120 52 L240 108" fill="none" stroke="#dfe2e5"/><path d="M0 0 Q60 12 120 30 Q180 12 240 0 L240 6 Q180 18 120 36 Q60 18 0 6Z" fill="var(--blue)"/><circle cx="120" cy="58" r="8" fill="var(--blue)"/></svg>
  </section>

</main>
</body>
</html>
```